Dune Air & Plus business card

I need an awesome, double-sided business card designed with our new logo. I would like the one side black with the colored logo, and the back side is all yours. I'd like to see horizontal and vertical layouts. Get creative! Thank you.

Target Market(s)

HVAC, Heating and Cooling in Phoenix, AZ

Industry/Entity Type

HVAC

Contact Information for Business Card

We need our new logo on the card. Tom Harker, (623) 555-0142, tom@trydunesair.com, www.trydunesair.com, ROC 514273

```html
<!DOCTYPE html>
<html lang="en">
<head>
<meta charset="utf-8">
<title>Dune Air &amp; Plus – Business Card</title>
<link href="https://fonts.googleapis.com/css2?family=Montserrat:wght@400;500;600;700&display=swap" rel="stylesheet">
<style>
  :root{
    --canvas:#ece7e1;
    --card-dark:#1f1311;
    --card-light:#ffffff;
    --gold-deep:#c48b0c;
    --gold-light:#ecd48a;
    --ink:#1b1b1b;
    --accent-orange:#f39a1e;
    --brand-blue:#2f7fd3;
    --icon-ring:#ffffff;
  }
  *{box-sizing:border-box;margin:0;padding:0}
  html,body{width:1200px;height:1200px;overflow:hidden;background:var(--canvas)}
  body{font-family:"Montserrat",sans-serif;position:relative}

  .card{
    position:absolute;left:180px;width:840px;height:480px;
    border-radius:4px;overflow:hidden;
    box-shadow:0 10px 28px rgba(0,0,0,.22);
  }
  .card--front{top:90px;background:var(--card-light)}
  .card--back{top:630px;background:var(--card-dark)}

  /* front */
  .front__brand-panel{
    position:absolute;left:0;top:0;width:345px;height:100%;
    background:var(--card-dark);
    display:flex;align-items:center;justify-content:center;
  }
  .brand-name{
    font-family:"Montserrat",sans-serif;font-weight:700;
    color:#ffffff;letter-spacing:.5px;white-space:nowrap;
  }
  .front__brand-panel .brand-name{font-size:29px}

  .front__gold-band{
    position:absolute;left:345px;top:0;width:65px;height:100%;
    background:linear-gradient(180deg,var(--gold-deep) 0%,var(--gold-light) 45%,var(--gold-deep) 100%);
  }

  .front__identity{position:absolute;left:445px;top:56px}
  .person-name{font-size:30px;font-weight:700;letter-spacing:2.5px;color:var(--ink);line-height:1.1}
  .person-role{font-size:22px;font-weight:600;letter-spacing:2.5px;color:var(--accent-orange);margin-top:6px}
  .person-license{font-size:17px;font-weight:600;letter-spacing:2px;color:var(--ink);margin-top:8px}

  .contact-list{position:absolute;left:376px;top:232px;list-style:none}
  .contact-item{display:flex;align-items:center;height:52px;margin-bottom:2px}
  .contact-icon{
    width:52px;height:52px;border-radius:50%;
    background:var(--icon-ring);
    display:flex;align-items:center;justify-content:center;
    box-shadow:0 0 0 2px rgba(0,0,0,.08);
  }
  .contact-icon svg{width:28px;height:28px}
  .contact-text{margin-left:30px;font-size:19px;font-weight:500;color:var(--ink);letter-spacing:.4px}

  /* back */
  .card--back{display:flex;align-items:center;justify-content:center}
  .back__brand{display:flex;align-items:center;gap:22px}
  .back__brand-dot{width:46px;height:46px;border-radius:50%;background:var(--accent-orange)}
  .card--back .brand-name{font-size:58px;color:var(--brand-blue)}
</style>
</head>
<body>

<section class="card card--front" aria-label="Business card front">
  <div class="front__brand-panel">
    <span class="brand-name">Dune Air &amp; Plus</span>
  </div>
  <div class="front__gold-band"></div>

  <div class="front__identity">
    <p class="person-name">TOM HARKER</p>
    <p class="person-role">OWNER</p>
    <p class="person-license">ROC 514273</p>
  </div>

  <ul class="contact-list">
    <li class="contact-item">
      <span class="contact-icon">
        <svg viewBox="0 0 24 24" aria-hidden="true"><path fill="#1b1b1b" d="M6.6 10.8a15.5 15.5 0 0 0 6.6 6.6l2.2-2.2c.3-.3.7-.4 1-.2 1.1.4 2.3.6 3.6.6.6 0 1 .4 1 1V20c0 .6-.4 1-1 1A17 17 0 0 1 3 4c0-.6.4-1 1-1h3.5c.6 0 1 .4 1 1 0 1.3.2 2.5.6 3.6.1.3 0 .7-.2 1z"/></svg>
      </span>
      <span class="contact-text">(623) 555-0142</span>
    </li>
    <li class="contact-item">
      <span class="contact-icon">
        <svg viewBox="0 0 24 24" aria-hidden="true" fill="none" stroke="#1b1b1b" stroke-width="1.4"><rect x="3" y="6" width="18" height="12"/><path d="M3 6l9 7 9-7M3 18l7-6M21 18l-7-6"/></svg>
      </span>
      <span class="contact-text">tom@trydunesair.com</span>
    </li>
    <li class="contact-item">
      <span class="contact-icon">
        <svg viewBox="0 0 24 24" aria-hidden="true" fill="none" stroke="#1b1b1b" stroke-width="1.2"><circle cx="12" cy="12" r="9"/><ellipse cx="12" cy="12" rx="4" ry="9"/><path d="M3 12h18M4.5 7.5h15M4.5 16.5h15M12 3v18"/></svg>
      </span>
      <span class="contact-text">www.trydunesair.com</span>
    </li>
  </ul>
</section>

<section class="card card--back" aria-label="Business card back">
  <div class="back__brand">
    <span class="back__brand-dot"></span>
    <span class="brand-name">Dune Air &amp; Plus</span>
  </div>
</section>

</body>
</html>
```